I teach courses in Quick Phrases for Rescue Crews, paramedics, firefighters, nurses and all other Emergency related occupations. I need to let them know that this course is available and post this card on the bulletin boards of fire stations and other related offices. It has to call their attention.

Industry/Entity Type

Call

Colors
ec2027

Requirements
Must have
• I would like a picture of a paramedic and a nurse. It can also have a firefighter as a second choice. Red is a good color to call attention. I am including a picture of me and a short bio to go on the reverse but this is not a must. I do not want my picture in the front.
I am thinking of an over sized postcard
Nice to have
• The title can be "Quick Phrases for Rescue Crews" in full or "Quick Phrases for RC's " depending on the fact that the whole name may be too long to make it stand out enough
Should not have
• I do not know if my picture has come out in the right frame I see the cut is not right in the uploead. You might need to frame it right.

```html
<!DOCTYPE html>
<html lang="en">
<head>
<meta charset="UTF-8">
<title>Quick Phrases for RC's</title>
<link rel="stylesheet" href="https://fonts.googleapis.com/css2?family=Anton&family=Archivo:wght@400;800&display=swap">
<style>
  :root {
    --brand-red: #ec2027;
    --deep-red: #8e0f14;
    --white: #ffffff;
    --ink: #111111;
    --frame-grey: #d9d9d9;
    --grass: #6f8f3a;
    --grass-light: #b7c98a;
    --uniform-red: #c8222a;
  }
  * { box-sizing: border-box; margin: 0; padding: 0; }
  html, body { width: 1200px; height: 776px; overflow: hidden; background: var(--white); }
  .postcard {
    position: relative;
    width: 1200px;
    height: 776px;
    background: var(--white);
    font-family: "Archivo", Arial, sans-serif;
    overflow: hidden;
  }
  .top-band {
    position: absolute;
    left: 0; top: 0;
    width: 1200px; height: 230px;
    background: var(--brand-red);
  }
  .course-title {
    position: absolute;
    left: 0; top: 22px;
    width: 1200px;
    text-align: center;
    font-family: "Anton", Impact, sans-serif;
    font-size: 112px;
    line-height: 1;
    letter-spacing: 1px;
    color: var(--white);
    text-transform: uppercase;
    text-shadow: 5px 5px 0 var(--deep-red);
  }
  .photo-frame {
    position: absolute;
    left: 44px; top: 163px;
    width: 846px; height: 574px;
    background: var(--frame-grey);
    box-shadow: 6px 6px 10px rgba(0,0,0,0.25);
    padding: 6px;
  }
  .photo-area {
    width: 100%; height: 100%;
    background:
      radial-gradient(ellipse at 45% 55%, var(--uniform-red) 0%, rgba(200,34,42,0.55) 30%, rgba(200,34,42,0) 55%),
      linear-gradient(180deg, #e8ece4 0%, var(--grass-light) 38%, var(--grass) 100%);
  }
  .audience-line {
    position: absolute;
    left: 243px; top: 176px;
    width: 640px;
    font-weight: 800;
    font-size: 23px;
    line-height: 1.12;
    color: var(--ink);
  }
  .contact-box {
    position: absolute;
    left: 64px; top: 630px;
    width: 370px; height: 86px;
    background: var(--brand-red);
    padding: 8px 10px;
    color: var(--white);
    font-weight: 800;
    font-size: 20.5px;
    line-height: 1.2;
  }
  .benefit-list {
    position: absolute;
    left: 874px; top: 244px;
    width: 312px;
    list-style: none;
    font-size: 19.5px;
    line-height: 1.22;
    color: var(--ink);
  }
  .benefit-list li {
    position: relative;
    padding-left: 20px;
    margin-bottom: 6px;
  }
  .benefit-list li::before {
    content: "";
    position: absolute;
    left: 0; top: 5px;
    width: 14px; height: 14px;
    background: var(--brand-red);
  }
</style>
</head>
<body>
<main class="postcard">
  <div class="top-band"></div>
  <h1 class="course-title">Quick Phrases for RC's</h1>

  <div class="photo-frame">
    <div class="photo-area" role="img" aria-label="Photo of a paramedic team in red uniforms kneeling on grass, tending to a patient lying on the ground"></div>
  </div>

  <p class="audience-line">Course designed specifically for paramedics, firefighters, nurses and all other emergency related occupations.</p>

  <p class="contact-box">For more information find us on Circlewall as Marisol Everett or call: 555-014-2290</p>

  <ul class="benefit-list">
    <li>Learn exactly the language you need for each emergency situation</li>
    <li>Bring down the language barrier with your Spanish-speaking patients</li>
    <li>Earn credits for your job or resume</li>
    <li>Meet new people while you practice</li>
    <li>Build a solid base for speaking Spanish in any situation sounding like a native</li>
    <li>Learn easily with “whole brain learning tools”</li>
    <li>Learn more about yourself and how you learn best</li>
    <li>Have great fun and de-stress</li>
  </ul>
</main>
</body>
</html>
```